Flyer-Design für Psychotherapeut
Zielgruppe
Angeboten wird als Dienstleistung Psychotherapie, Coaching und Paarberatung
für Einzelpersonen (Männer/Frauen), Paare und Familien in schwierigen privaten und beruflichen Lebenssituationen.
Aufgabenstellung
Sehr geehrte Damen, sehr geehrte Herren,
gewünscht wird ein Falzflyer Hochformat, DIN-Lang, Wickelfalz, 6 bedruckte Seiten mit dem Endformat 10,0 x 21,0 cm. Ein entsprechendes Datenblatt der Druckerei finden Sie im Anhang.
Der Flyer wird auf einer Gesundheitsmesse eingesetzt und soll einen Überblick über mein Dienstleistungsangebot geben.
In der beigefügten Word Datei finden Sie einen von mir erstellten Flyer-Text-Entwurf. Er soll lediglich als Orientierung dienen. Weitere Infos erhalten Sie auf meiner Homepage
www.praxis-tollring-quast.de.
Desweiteren erhalten Sie ein hochgeladenes Foto von mir, welches Sie bitte in Ihren Entwurf mit einbinden.
Ich bitte um Vorschläge für ein professionelles Design mit moderener gut lesbarer Schrift sowie farblich abgestimmten Blöcken des Inhalts.
Besonders wichtig ist mir die Orientierung an meinen Logofarben.
Das Logo wurde auch von gestaltwerk.de erstellt. Sie finden es unter meinen Projekten.
Für Rückfragen stehe ich Ihnen gerne zur Verfügung.
Freundliche Grüße
Sabine Tollring-Quast

```html
<!DOCTYPE html>
<html lang="de">
<head>
<meta charset="utf-8">
<title>Flyer Sabine Tollring-Quast</title>
<link href="https://fonts.googleapis.com/css2?family=Ubuntu:wght@400;500;700&display=swap" rel="stylesheet">
<style>
:root{
  --orange:#e8501a;
  --orange-deep:#d9401a;
  --orange-light:#f07a2a;
  --peach:#f9cfb4;
  --peach-soft:#fde9dc;
  --text:#4a4a4a;
  --grey:#6d6d6d;
  --grey-light:#c9bcb2;
  --bg:#ebebeb;
  --paper:#ffffff;
}
*{margin:0;padding:0;box-sizing:border-box}
html,body{width:859px;height:1200px;overflow:hidden;background:var(--bg)}
body{font-family:"Ubuntu",Arial,sans-serif;color:var(--text);position:relative}
.sheet{position:absolute;left:42px;width:775px;height:548px;background:var(--paper);overflow:hidden}
.sheet--outside{top:38px}
.sheet--inside{top:615px}
.abs{position:absolute}
.photo{position:absolute}
.h-main{font-weight:700;color:var(--orange-deep);font-size:16.5px;letter-spacing:-.2px;line-height:1.1}
.h-sub{font-weight:400;color:var(--orange-deep);font-size:10.5px;line-height:1.5;text-transform:uppercase}
.ticks{list-style:none;font-size:8px;line-height:1.38}
.ticks li{position:relative;padding-left:18px;margin-bottom:5.5px}
.ticks li::before{content:"✔";position:absolute;left:0;top:-1px;color:var(--orange-deep);font-size:10px}
.body{font-size:8px;line-height:1.45;text-align:left}
.peach-fade{position:absolute;background:linear-gradient(to bottom,var(--peach) 0%,var(--peach-soft) 45%,#fff 100%)}
.badge{position:absolute;left:371px;top:150px;width:106px;height:106px;border-radius:50%;background:radial-gradient(circle at 40% 35%,var(--orange-light),var(--orange-deep));box-shadow:0 0 0 4px #fbe3d4;color:#fff;font-weight:500;font-size:9.5px;line-height:1.35;text-align:center;display:flex;align-items:center;justify-content:center;transform:rotate(-12deg)}
.portrait{left:286px;top:231px;width:75px;height:75px;border-radius:9px;background:linear-gradient(160deg,#e4e4e4,#a9a9a9 55%,#7a7a7a)}
.contact{left:286px;top:316px;width:210px;font-size:8px;line-height:1.45}
.contact .name{color:var(--orange-deep);font-weight:700;font-size:9px}
.contact p{margin-bottom:6px}
.brand{left:540px;top:34px;width:225px;text-align:right}
.brand-name{font-size:17px;color:var(--grey);font-weight:400}
.brand-tag{font-size:8px;color:var(--orange);margin-top:3px}
.slogan{left:545px;top:370px;width:220px;text-align:center;font-size:23px;line-height:1.4;color:var(--grey)}
.slogan b{color:var(--orange-deep);font-weight:700}
.claim{left:544px;top:474px;font-size:17px;line-height:1.6;color:var(--orange-deep)}
.url{right:320px;top:522px;font-size:13px;font-weight:700;color:var(--orange-deep)}
.rule{left:0;top:516px;width:455px;height:1px;background:var(--orange)}
</style>
</head>
<body>

<section class="sheet sheet--outside">
  <div class="photo" style="left:0;top:0;width:253px;height:190px;background:linear-gradient(100deg,#6f6460 0%,#b3a79e 30%,#e9e2dc 62%,#f3eee9 80%,#cfc5bd 100%)" role="img" aria-label="Foto: nachdenkliche Frau, im Hintergrund ein Mann"></div>
  <div class="photo" style="left:253px;top:0;width:261px;height:190px;background:linear-gradient(100deg,#9a8f88 0%,#dcd6d1 30%,#f1eeeb 55%,#e6d9da 80%,#b9aca6 100%)" role="img" aria-label="Foto: Mann mit verschränkten Armen auf dem Sofa"></div>
  <div class="peach-fade" style="left:0;top:190px;width:514px;height:320px"></div>

  <svg class="abs" style="left:0;top:0" width="775" height="200" viewBox="0 0 775 200">
    <path d="M0 0H775V16C560 8 300 30 0 62Z" fill="var(--orange)"/>
    <path d="M0 68C250 36 500 18 775 16" fill="none" stroke="#fff" stroke-width="6" opacity=".55"/>
    <path d="M0 82C250 48 500 28 775 26" fill="none" stroke="var(--orange)" stroke-width="1.2"/>
    <path d="M0 122C200 96 400 72 514 62" fill="none" stroke="var(--orange)" stroke-width="1.2"/>
  </svg>

  <div class="photo" style="left:514px;top:73px;width:261px;height:270px;background:linear-gradient(to bottom,#c9d7a0 0%,#8fa15a 18%,#a4784c 42%,#8a5b38 70%,#b48a66 88%,#d8c4b0 100%)" role="img" aria-label="Foto: Holztreppe im Grünen, die nach oben führt"></div>
  <svg class="abs" style="left:514px;top:0" width="261" height="470" viewBox="0 0 261 470">
    <path d="M0 0H261V36C170 20 80 12 0 12Z" fill="var(--orange)"/>
    <path d="M0 14C80 14 170 22 261 38V112C170 88 90 76 0 73Z" fill="#fff"/>
    <path d="M0 73C90 76 170 88 261 112" fill="none" stroke="var(--orange)" stroke-width="1.5"/>
    <path d="M0 343C90 338 180 338 261 343V412C180 430 80 430 0 418Z" fill="#e6e0dc"/>
    <path d="M0 343C90 338 180 338 261 343" fill="none" stroke="var(--orange)" stroke-width="2"/>
    <path d="M0 420C80 432 180 432 261 414" fill="none" stroke="var(--orange)" stroke-width="1.5"/>
  </svg>

  <div class="abs brand">
    <div class="brand-name">Sabine Tollring-Quast</div>
    <div class="brand-tag">Psychotherapie &nbsp;| Coaching | Paarberatung</div>
  </div>
  <div class="abs slogan">AUS<b>WEGE</b><br>LÖSUNGS<b>WEGE</b></div>
  <div class="abs claim">Für mehr Zufriedenheit<br>im Privatleben und Beruf</div>

  <div class="abs" style="left:33px;top:201px;width:210px">
    <h2 class="h-main">PAARBERATUNG –</h2>
    <h3 class="h-sub" style="margin:9px 0 10px">Unterstützung für Paare<br>in Krisenzeiten</h3>
    <ul class="ticks">
      <li>Wenn Sie das Gefühl haben aneinander vorbei zu reden.</li>
      <li>Wenn Ihr Beziehungsalltag von Streitereien und Konflikten bestimmt wird.</li>
      <li>Wenn Sie Ihre gemeinsame Intimität und Sexualität verloren haben</li>
      <li>Wenn eine Affäre Ihre Beziehung erschüttert hat.</li>
      <li>Wenn nach der Geburt von Kindern, durch Arbeitslosigkeit oder Krankheit Probleme in Ihrer Beziehung entstanden sind</li>
      <li>Wenn das Leben in der Patchwork-Familie Ihre Beziehung belastet</li>
    </ul>
    <h3 class="h-sub" style="margin:18px 0 10px">Trennungsbegleitung<br>und Mediation</h3>
    <ul class="ticks"><li>Wenn Sie über Trennung nachdenken.</li></ul>
  </div>

  <div class="badge">Haben Sie Fragen?<br>Rufen Sie mich an.<br>Ich bin für Sie da.</div>
  <div class="photo portrait" role="img" aria-label="Porträtfoto von Sabine Tollring-Quast"></div>
  <div class="abs contact">
    <p><span class="name">SABINE TOLLRING-QUAST</span><br>Heilpraktikerin Psychotherapie (HeilprG)<br>Systemischer Coach (DVSC)</p>
    <p>Am Lindenhof 14<br>64579 Feldbrunn</p>
    <p>Telefon 06152 – 493817<br>info@praxis-tollring-quast.de</p>
    <p style="margin-top:12px">Rufen Sie mich an. Ich bin für Sie da!<br>Ich freue mich auf Ihren Besuch!</p>
    <p style="margin-top:14px;font-size:9.5px;line-height:1.3"><span class="h-sub" style="font-size:10.5px">Weitere Informationen</span><br>über mich und meine Angebote finden<br>Sie auf meiner Homepage.</p>
  </div>
  <div class="abs rule"></div>
  <div class="abs url">www.praxis-tollring.de</div>
</section>

<section class="sheet sheet--inside">
  <div class="peach-fade" style="left:0;top:190px;width:260px;height:358px"></div>
  <div class="peach-fade" style="left:260px;top:60px;width:261px;height:488px"></div>
  <div class="peach-fade" style="left:521px;top:20px;width:254px;height:528px"></div>
  <div class="photo" style="left:0;top:25px;width:260px;height:168px;background:linear-gradient(100deg,#c8b0b8 0%,#d9c3c0 35%,#ecdccd 60%,#e2c8b0 80%,#d6bea6 100%)" role="img" aria-label="Foto: erschöpfte Frau hält sich den Kopf"></div>

  <svg class="abs" style="left:0;top:0" width="775" height="100" viewBox="0 0 775 100">
    <path d="M0 0H775V34C700 16 600 10 521 12C400 12 320 20 260 28C160 40 60 58 0 76Z" fill="var(--orange)"/>
    <path d="M260 34C340 22 440 18 522 17V64C440 58 340 58 260 62Z" fill="var(--grey-light)"/>
    <path d="M0 90C80 66 170 48 260 38" fill="none" stroke="#fff" stroke-width="6" opacity=".6"/>
    <path d="M0 96C80 72 170 56 260 48" fill="none" stroke="var(--orange)" stroke-width="1.2"/>
    <path d="M260 62C340 58 440 58 522 66" fill="none" stroke="var(--orange)" stroke-width="1.2"/>
    <path d="M300 20C450 6 650 8 775 30" fill="none" stroke="#fff" stroke-width="1.5"/>
  </svg>

  <div class="abs" style="left:33px;top:206px;width:215px">
    <h2 class="h-main">SIE WÜNSCHEN SICH …</h2>
    <h3 class="h-sub" style="margin:9px 0 10px">Entlastung und<br>positive Veränderung weil …</h3>
    <ul class="ticks">
      <li>Sie sich in einer akuten privaten oder beruflichen Krisensituation befinden.</li>
      <li>Sie Probleme in Ihrer Partnerschaft haben.</li>
      <li>Sie mit Stress besser umgehen wollen.</li>
      <li>Sie sich antriebslos- und lustlos, erschöpft oder ständig überfordert fühlen.</li>
      <li>Sie unter Ängsten oder Panikattacken leiden, die Sie belasten und einschränken.</li>
    </ul>
    <p class="body" style="margin-top:36px">Jeder Mensch kommt im Leben in Situationen, die Unzufriedenheit, Überforderung und seelische Belastungen auslösen.</p>
    <p class="body" style="margin-top:10px">Wenn Veränderung nicht alleine gelingt, können Psychotherapie, Coaching oder Paarberatung eine große Hilfe sein, um Lösungswege aus diesen belastenden Situationen zu finden.</p>
  </div>

  <div class="abs" style="left:288px;top:78px;width:205px">
    <h2 class="h-main">MEIN ANGEBOT FÜR SIE</h2>
    <h3 class="h-sub" style="margin:9px 0 10px">Beratung- und Gesprächs-<br>therapie nach Karl Rohwer</h3>
    <h3 class="h-sub" style="margin-bottom:10px">Systemisches Coaching und<br>Paarberatung</h3>
    <p class="body">Als erfahrene Therapeutin, Beraterin und Coach begleite ich Sie als Einzelperson, Paar oder Familie in schwierigen Lebenssituationen und Neuorientierungsphasen.</p>
    <p class="body" style="margin-top:10px">Ich unterstütze Sie einfühlsam und lösungsorientiert. Dabei nutze ich anerkannte, wirksame Therapie- und Beratungsmethoden, die ich gemeinsam mit Ihnen, auf Ihre persönlichen Bedürfnisse und Ziele abstimme.</p>
    <p class="body" style="margin-top:10px">Im Mittelpunkt stehen Sie mit Ihrem Anliegen.</p>
    <p class="body" style="margin-top:10px">Wir begegnen uns in einer Atmosphäre der Wertschätzung, Anteilnahme und absoluten Diskretion.</p>
    <h2 class="h-main" style="margin:24px 0 10px">SIE KÖNNEN …</h2>
    <ul class="ticks">
      <li>Bewältigungsstrategien entwickeln</li>
      <li>Ihre Fähigkeiten und Stärken entdecken</li>
      <li>Innere Blockaden überwinden</li>
      <li>Ihr Selbstvertrauen steigern</li>
      <li>Sich mutig und motiviert an Neues heranwagen</li>
      <li>Ihre Ziele umsetzen</li>
      <li>Ihr Leben und Ihre Partnerschaft so gestalten, wie Sie es sich wünschen.</li>
    </ul>
  </div>

  <div class="abs" style="left:546px;top:30px;width:210px">
    <h2 class="h-main">PSYCHOTHERAPIE</h2>
    <h3 class="h-sub" style="margin:9px 0 8px">Meine Behandlungsschwerpunkte:</h3>
    <ul class="ticks">
      <li>Ängste- und Panikattacken</li>
      <li>Depression</li>
      <li>Erschöpfung/Burnout</li>
      <li>Reaktion auf schwere Belastungen</li>
      <li>Psychosomatische Beschwerden</li>
      <li>Psychoonkologie</li>
      <li>Lindauer Gesundheitstraining</li>
    </ul>
    <h2 class="h-main" style="margin-top:20px">COACHING</h2>
    <h3 class="h-sub" style="margin:9px 0 10px">Begleitung in Veränderung-<br>sprozessen und schwierigen<br>Lebensphasen/-krisen</h3>
    <ul class="ticks">
      <li>Veränderte Rahmenbedingungen im Privat- und Berufsleben wie z.B. Krankheit, Trennung, Trauer, Mobbing, Arbeitsplatzverlust u.a.</li>
      <li>Berufliche Neuorientierung</li>
      <li>Entscheidungsfindung</li>
      <li>Zielsetzung und Realisierung</li>
      <li>Lebensumbrüche wie z.B. Wechseljahre, Pensionierung u.a.</li>
    </ul>
    <h3 class="h-sub" style="margin:12px 0 10px">Persönlichkeitsentwicklung</h3>
    <ul class="ticks">
      <li>Konflikte erkennen und konstruktiv lösen</li>
      <li>Beziehungs- und Lebensgestaltung</li>
      <li>Eigene Stärken entdecken, weiter entwickeln und nutzen</li>
      <li>Stressbewältigung/Burnoutprävention</li>
    </ul>
  </div>
</section>

</body>
</html>
```